Chill Bo
frozen yogurt and more
Corporate
Tara Kessler
Owner
4182 Larkspur Ln.
Columbus IN. 47358
tarasglow@quillpost.com
Don't have store open yet so have no address or phone numbers. We want logo font the same but would like a standard clean font for the rest of the info

```html
<!DOCTYPE html>
<html lang="en">
<head>
<meta charset="utf-8">
<title>Chill Bo – Business Card</title>
<link rel="stylesheet" href="https://fonts.googleapis.com/css2?family=Open+Sans:wght@400;600;700&display=swap">
<style>
  :root {
    --backdrop: #ece7df;
    --card: #ffffff;
    --brown: #5a3516;
    --green: #6cb33f;
    --ink: #3b3b3b;
    --rule: #d6d6d6;
  }
  * { margin: 0; padding: 0; box-sizing: border-box; }
  html, body {
    width: 1200px;
    height: 780px;
    overflow: hidden;
    background: var(--backdrop);
    font-family: "Open Sans", Arial, sans-serif;
  }
  .card {
    position: absolute;
    left: 80px;
    top: 90px;
    width: 1040px;
    height: 600px;
    border-radius: 26px;
    overflow: hidden;
    background: var(--card);
    box-shadow: 0 6px 18px rgba(0,0,0,0.18);
  }
  .card-edges {
    position: absolute;
    inset: 0;
  }
  .brand {
    position: absolute;
    left: 150px;
    top: 200px;
    width: 360px;
    display: flex;
    flex-direction: column;
    align-items: center;
    gap: 14px;
  }
  .brand-mark {
    display: flex;
    align-items: center;
    gap: 20px;
  }
  .brand-dot {
    width: 50px;
    height: 50px;
    border-radius: 50%;
    background: var(--green);
  }
  .brand-name {
    font-size: 66px;
    font-weight: 600;
    color: var(--brown);
    line-height: 1;
  }
  .brand-tagline {
    font-size: 19px;
    font-weight: 400;
    color: var(--green);
    text-transform: uppercase;
    letter-spacing: 3px;
    white-space: nowrap;
  }
  .divider {
    position: absolute;
    left: 540px;
    top: 120px;
    width: 2px;
    height: 360px;
    background: linear-gradient(to bottom, rgba(214,214,214,0), var(--rule) 20%, var(--rule) 80%, rgba(214,214,214,0));
  }
  .contact {
    position: absolute;
    left: 572px;
    top: 120px;
    color: var(--ink);
  }
  .contact-name {
    font-size: 28px;
    font-weight: 700;
    color: var(--brown);
  }
  .contact-role {
    font-size: 22px;
    font-weight: 600;
    color: var(--green);
    margin-top: 2px;
  }
  .contact-address {
    margin-top: 70px;
    font-size: 20px;
    line-height: 1.4;
  }
  .contact-lines {
    margin-top: 48px;
    list-style: none;
    font-size: 20px;
  }
  .contact-lines li {
    display: flex;
    align-items: center;
    gap: 12px;
  }
  .contact-lines svg { flex: none; }
</style>
</head>
<body>
  <div class="card">
    <svg class="card-edges" width="1040" height="600" viewBox="0 0 1040 600" aria-hidden="true">
      <path d="M0,0 L22,0 Q62,300 118,600 L0,600 Z" fill="var(--brown)"/>
      <path d="M36,0 Q80,300 148,600" fill="none" stroke="var(--green)" stroke-width="7"/>
      <path d="M1040,0 L950,0 Q1005,300 1022,600 L1040,600 Z" fill="var(--brown)"/>
      <path d="M918,0 Q978,300 1000,600" fill="none" stroke="var(--green)" stroke-width="7"/>
    </svg>

    <div class="brand">
      <div class="brand-mark">
        <span class="brand-dot"></span>
        <span class="brand-name">Chill Bo</span>
      </div>
      <p class="brand-tagline">frozen yogurt and more</p>
    </div>

    <div class="divider"></div>

    <div class="contact">
      <p class="contact-name">Tara Kessler</p>
      <p class="contact-role">Owner</p>
      <p class="contact-address">4182 Larkspur Ln.<br>Columbus IN. 47358</p>
      <ul class="contact-lines">
        <li>
          <svg width="20" height="16" viewBox="0 0 24 18" aria-label="Email"><rect x="1" y="1" width="22" height="16" rx="2" fill="var(--ink)"/><path d="M2 2 L12 10 L22 2" fill="none" stroke="#fff" stroke-width="2"/></svg>
          <span>tarasglow@quillpost.com</span>
        </li>
      </ul>
    </div>
  </div>
</body>
</html>
```